Custom Mexican Train Dominos Scorecard

My wife and I regularly play Mexican Train dominos with our friends and family and would like to create a series of custom scorecards specific to our various groups that we play with. The idea would be to have them printed on pads or in notebooks that over time will hold a record of all of our games. Searching around on the web, the only "off the shelf" that I see are pretty plain and boring (see attached). We would love something with a fun and playful mid-century graphic feel to it. Can be a single color or more than one. We want to have the player names incorporated into the design, so for the first one the names would be Tessa, Harold, Ruth & Colin. We will want a place to date each card and of course boxes to fill out the score. I have included a few examples of how the scorecard is basically laid out. Can be any size and can be done in landscape or portrait. I think I would just like the title to say "Domino Night" or potentially no title at all with just a fun domino graphic. Thank you!

Requirements
Must have
• Basic score layout
Nice to have
• nothing in particular
Should not have
• nothing in particular

```html
<!DOCTYPE html>
<html lang="en">
<head>
<meta charset="utf-8">
<title>Domino Night Scorecard</title>
<link rel="stylesheet" href="https://fonts.googleapis.com/css2?family=Bungee+Inline&family=Mouse+Memoirs&family=Sniglet:wght@800&display=swap">
<style>
  :root {
    --paper: #f4e8d8;
    --paper-edge: #e9d6bf;
    --ink: #8e3b40;
    --ink-soft: #9a4a4e;
    --rule: #b9ada2;
    --pip: #f7ece0;
  }
  * { box-sizing: border-box; margin: 0; padding: 0; }
  html, body { width: 859px; height: 1200px; overflow: hidden; }
  body {
    position: relative;
    background: radial-gradient(ellipse at 55% 45%, var(--paper) 55%, var(--paper-edge) 100%);
    color: var(--ink);
    font-family: "Mouse Memoirs", sans-serif;
  }
  .train-art {
    position: absolute; left: 4px; top: 10px; width: 192px; height: 138px;
    background: radial-gradient(ellipse at 45% 60%, rgba(142,59,64,0.45), rgba(142,59,64,0.12) 70%, transparent 75%);
  }
  .title {
    position: absolute; left: 246px; top: 58px; width: 380px;
    font-family: "Bungee Inline", sans-serif; font-size: 41px; font-weight: 400;
    letter-spacing: -1px; color: var(--ink-soft); text-align: center; white-space: nowrap;
  }
  .scorecard { position: absolute; left: 28px; top: 149px; width: 815px; border-collapse: collapse; table-layout: fixed; }
  .scorecard td, .scorecard th { border: 1px solid var(--rule); }
  .scorecard th {
    height: 72px; font-weight: 400; font-size: 28px; letter-spacing: 0.5px;
    text-transform: uppercase; color: var(--ink);
  }
  .scorecard th.label-head { text-align: left; padding-left: 30px; }
  .scorecard td { height: 61.6px; }
  .tile-label { padding-left: 20px; }
  .tile-label .wrap { display: flex; align-items: center; }
  .tile-label svg { width: 98px; height: 46px; display: block; }
  .tile-label .count {
    font-family: "Sniglet", sans-serif; font-weight: 800; font-size: 27px;
    color: var(--ink); font-style: italic; width: 70px; text-align: center;
  }
  .tile-label .count.low { width: 90px; }
  .row-label { font-size: 28px; padding-left: 34px; text-transform: uppercase; }
  .game-total { position: absolute; left: 28px; top: 1087px; width: 815px; border-collapse: collapse; table-layout: fixed; }
  .game-total td { height: 50px; border: 1px solid var(--rule); }
  .game-total .row-label { padding-left: 26px; }
  .date-label { position: absolute; left: 646px; top: 1146px; font-size: 30px; text-transform: uppercase; }
  .tile { fill: var(--ink); }
  .pip { fill: var(--pip); }
</style>
</head>
<body>
<svg width="0" height="0" style="position:absolute">
  <defs>
    <g id="pips-12" class="pip"><circle cx="12" cy="15" r="4.5"/><circle cx="24" cy="15" r="4.5"/><circle cx="36" cy="15" r="4.5"/><circle cx="48" cy="15" r="4.5"/><circle cx="12" cy="30" r="4.5"/><circle cx="24" cy="30" r="4.5"/><circle cx="36" cy="30" r="4.5"/><circle cx="48" cy="30" r="4.5"/><circle cx="12" cy="45" r="4.5"/><circle cx="24" cy="45" r="4.5"/><circle cx="36" cy="45" r="4.5"/><circle cx="48" cy="45" r="4.5"/></g>
    <g id="pips-11" class="pip"><circle cx="12" cy="15" r="4.5"/><circle cx="24" cy="15" r="4.5"/><circle cx="36" cy="15" r="4.5"/><circle cx="48" cy="15" r="4.5"/><circle cx="18" cy="30" r="4.5"/><circle cx="30" cy="30" r="4.5"/><circle cx="42" cy="30" r="4.5"/><circle cx="12" cy="45" r="4.5"/><circle cx="24" cy="45" r="4.5"/><circle cx="36" cy="45" r="4.5"/><circle cx="48" cy="45" r="4.5"/></g>
    <g id="pips-10" class="pip"><circle cx="12" cy="15" r="4.5"/><circle cx="24" cy="15" r="4.5"/><circle cx="36" cy="15" r="4.5"/><circle cx="48" cy="15" r="4.5"/><circle cx="12" cy="30" r="4.5"/><circle cx="48" cy="30" r="4.5"/><circle cx="12" cy="45" r="4.5"/><circle cx="24" cy="45" r="4.5"/><circle cx="36" cy="45" r="4.5"/><circle cx="48" cy="45" r="4.5"/></g>
    <g id="pips-9" class="pip"><circle cx="15" cy="15" r="5"/><circle cx="30" cy="15" r="5"/><circle cx="45" cy="15" r="5"/><circle cx="15" cy="30" r="5"/><circle cx="30" cy="30" r="5"/><circle cx="45" cy="30" r="5"/><circle cx="15" cy="45" r="5"/><circle cx="30" cy="45" r="5"/><circle cx="45" cy="45" r="5"/></g>
    <g id="pips-8" class="pip"><circle cx="15" cy="15" r="5"/><circle cx="30" cy="15" r="5"/><circle cx="45" cy="15" r="5"/><circle cx="15" cy="30" r="5"/><circle cx="45" cy="30" r="5"/><circle cx="15" cy="45" r="5"/><circle cx="30" cy="45" r="5"/><circle cx="45" cy="45" r="5"/></g>
    <g id="pips-7" class="pip"><circle cx="15" cy="15" r="5"/><circle cx="30" cy="15" r="5"/><circle cx="45" cy="15" r="5"/><circle cx="30" cy="30" r="5"/><circle cx="15" cy="45" r="5"/><circle cx="30" cy="45" r="5"/><circle cx="45" cy="45" r="5"/></g>
    <g id="pips-6" class="pip"><circle cx="15" cy="18" r="5"/><circle cx="30" cy="18" r="5"/><circle cx="45" cy="18" r="5"/><circle cx="15" cy="42" r="5"/><circle cx="30" cy="42" r="5"/><circle cx="45" cy="42" r="5"/></g>
    <g id="pips-5" class="pip"><circle cx="16" cy="16" r="5"/><circle cx="44" cy="16" r="5"/><circle cx="30" cy="30" r="5"/><circle cx="16" cy="44" r="5"/><circle cx="44" cy="44" r="5"/></g>
    <g id="pips-4" class="pip"><circle cx="16" cy="16" r="5"/><circle cx="44" cy="16" r="5"/><circle cx="16" cy="44" r="5"/><circle cx="44" cy="44" r="5"/></g>
    <g id="pips-3" class="pip"><circle cx="16" cy="16" r="5"/><circle cx="30" cy="30" r="5"/><circle cx="44" cy="44" r="5"/></g>
    <g id="pips-2" class="pip"><circle cx="16" cy="16" r="5"/><circle cx="44" cy="44" r="5"/></g>
    <g id="pips-1" class="pip"><circle cx="30" cy="30" r="5"/></g>
    <g id="pips-0"></g>
  </defs>
</svg>

<div class="train-art" role="img" aria-label="Vintage steam locomotive illustration"></div>
<h1 class="title">Domino Night</h1>

<table class="scorecard">
  <colgroup><col style="width:229px"><col style="width:150px"><col style="width:140px"><col style="width:151px"><col style="width:145px"></colgroup>
  <thead>
    <tr><th class="label-head">Player Names</th><th>Tessa</th><th>Harold</th><th>Ruth</th><th>Colin</th></tr>
  </thead>
  <tbody>
    <tr><td class="tile-label"><div class="wrap"><svg viewBox="0 0 128 60"><rect class="tile" x="0" y="0" width="60" height="60" rx="9"/><rect class="tile" x="66" y="0" width="60" height="60" rx="9"/><use href="#pips-12"/><use href="#pips-12" x="66"/></svg><span class="count">12</span></div></td><td></td><td></td><td></td><td></td></tr>
    <tr><td class="tile-label"><div class="wrap"><svg viewBox="0 0 128 60"><rect class="tile" x="0" y="0" width="60" height="60" rx="9"/><rect class="tile" x="66" y="0" width="60" height="60" rx="9"/><use href="#pips-11"/><use href="#pips-11" x="66"/></svg><span class="count">11</span></div></td><td></td><td></td><td></td><td></td></tr>
    <tr><td class="tile-label"><div class="wrap"><svg viewBox="0 0 128 60"><rect class="tile" x="0" y="0" width="60" height="60" rx="9"/><rect class="tile" x="66" y="0" width="60" height="60" rx="9"/><use href="#pips-10"/><use href="#pips-10" x="66"/></svg><span class="count">10</span></div></td><td></td><td></td><td></td><td></td></tr>
    <tr><td class="tile-label"><div class="wrap"><svg viewBox="0 0 128 60"><rect class="tile" x="0" y="0" width="60" height="60" rx="9"/><rect class="tile" x="66" y="0" width="60" height="60" rx="9"/><use href="#pips-9"/><use href="#pips-9" x="66"/></svg><span class="count">9</span></div></td><td></td><td></td><td></td><td></td></tr>
    <tr><td class="tile-label"><div class="wrap"><svg viewBox="0 0 128 60"><rect class="tile" x="0" y="0" width="60" height="60" rx="9"/><rect class="tile" x="66" y="0" width="60" height="60" rx="9"/><use href="#pips-8"/><use href="#pips-8" x="66"/></svg><span class="count">8</span></div></td><td></td><td></td><td></td><td></td></tr>
    <tr><td class="tile-label"><div class="wrap"><svg viewBox="0 0 128 60"><rect class="tile" x="0" y="0" width="60" height="60" rx="9"/><rect class="tile" x="66" y="0" width="60" height="60" rx="9"/><use href="#pips-7"/><use href="#pips-7" x="66"/></svg><span class="count">7</span></div></td><td></td><td></td><td></td><td></td></tr>
    <tr><td class="tile-label"><div class="wrap"><svg viewBox="0 0 128 60"><rect class="tile" x="0" y="0" width="60" height="60" rx="9"/><rect class="tile" x="66" y="0" width="60" height="60" rx="9"/><use href="#pips-6"/><use href="#pips-6" x="66"/></svg><span class="count">6</span></div></td><td></td><td></td><td></td><td></td></tr>
    <tr><td class="row-label">Sub Total</td><td></td><td></td><td></td><td></td></tr>
    <tr><td class="tile-label"><div class="wrap"><svg viewBox="0 0 128 60"><rect class="tile" x="0" y="0" width="60" height="60" rx="9"/><rect class="tile" x="66" y="0" width="60" height="60" rx="9"/><use href="#pips-5"/><use href="#pips-5" x="66"/></svg><span class="count low">5</span></div></td><td></td><td></td><td></td><td></td></tr>
    <tr><td class="tile-label"><div class="wrap"><svg viewBox="0 0 128 60"><rect class="tile" x="0" y="0" width="60" height="60" rx="9"/><rect class="tile" x="66" y="0" width="60" height="60" rx="9"/><use href="#pips-4"/><use href="#pips-4" x="66"/></svg><span class="count low">4</span></div></td><td></td><td></td><td></td><td></td></tr>
    <tr><td class="tile-label"><div class="wrap"><svg viewBox="0 0 128 60"><rect class="tile" x="0" y="0" width="60" height="60" rx="9"/><rect class="tile" x="66" y="0" width="60" height="60" rx="9"/><use href="#pips-3"/><use href="#pips-3" x="66"/></svg><span class="count low">3</span></div></td><td></td><td></td><td></td><td></td></tr>
    <tr><td class="tile-label"><div class="wrap"><svg viewBox="0 0 128 60"><rect class="tile" x="0" y="0" width="60" height="60" rx="9"/><rect class="tile" x="66" y="0" width="60" height="60" rx="9"/><use href="#pips-2"/><use href="#pips-2" x="66"/></svg><span class="count low">2</span></div></td><td></td><td></td><td></td><td></td></tr>
    <tr><td class="tile-label"><div class="wrap"><svg viewBox="0 0 128 60"><rect class="tile" x="0" y="0" width="60" height="60" rx="9"/><rect class="tile" x="66" y="0" width="60" height="60" rx="9"/><use href="#pips-1"/><use href="#pips-1" x="66"/></svg><span class="count low">1</span></div></td><td></td><td></td><td></td><td></td></tr>
    <tr><td class="tile-label"><div class="wrap"><svg viewBox="0 0 128 60"><rect class="tile" x="0" y="0" width="60" height="60" rx="9"/><rect class="tile" x="66" y="0" width="60" height="60" rx="9"/><use href="#pips-0"/><use href="#pips-0" x="66"/></svg><span class="count low">0</span></div></td><td></td><td></td><td></td><td></td></tr>
  </tbody>
</table>

<table class="game-total">
  <colgroup><col style="width:229px"><col style="width:150px"><col style="width:140px"><col style="width:151px"><col style="width:145px"></colgroup>
  <tr><td class="row-label">Game Total</td><td></td><td></td><td></td><td></td></tr>
</table>

<div class="date-label">Date</div>
</body>
</html>
```